Melbourne Locksmith Needs a Web Site

We need a web site for our new Locksmith business in Melbourne Australia. Our business is called " Corbett Row Locksmiths" . (Corbett row is a well known in the city and has the famous railway station , it is a main icon of melbourne . Maybe we could incorperate the station maybe in the front page or heading background. our services include Automotive Locksmithing ( Cuting keys to cars, opening cars etc / Master Keys Systems/ Commercial work / Domestic . Also we have no logo yet. but we can get that in the future if needed.

Target Market(s)

(Automotive ) Lost keys to cars, Trucks, Jammed Ignitions, Opening Vehicles. mobile locksmith in a van, Locked out of your house ?

Industry/Entity Type

Business

Number of Pages Required

4 page

Font styles to use
Sans Serif

Colors

Designer to choose colors to be used in the design.

Requirements
Must have
• Phone number easy to read on web site.
Nice to have
• map of where we are, show case pictures of common lock problems for automotive eg ( damaged keys/ Broken).

```html
<!DOCTYPE html>
<html lang="en">
<head>
<meta charset="utf-8">
<title>Corbett Row Locksmiths</title>
<link href="https://fonts.googleapis.com/css2?family=Poppins:wght@300;400;500;600&family=Oswald:wght@400;500&display=swap" rel="stylesheet">
<style>
:root{
  --navy:#1e2135;
  --navy-deep:#171a2b;
  --blue:#2c4bd1;
  --blue-bright:#3b5fe0;
  --white:#ffffff;
  --ink:#222431;
  --grey:#6b6d78;
  --light:#ececef;
  --line:#d6d8df;
}
*{margin:0;padding:0;box-sizing:border-box}
html,body{width:1200px;height:3629px;overflow:hidden}
body{font-family:'Poppins',sans-serif;color:var(--ink);background:var(--white);position:relative}
.abs{position:absolute}
.photo{position:absolute}
.pill-btn{position:absolute;display:flex;align-items:center;justify-content:center;border-radius:20px;font-size:13px}
.arrow-btn{position:absolute;width:36px;height:36px;border-radius:50%;display:flex;align-items:center;justify-content:center}
.arrow-btn.blue{background:var(--blue)}
.arrow-btn.dark{background:#3a3d4d}
.arrow-btn.white{background:var(--white);border:1px solid var(--line)}
.section-title{position:absolute;left:0;width:1200px;text-align:center;font-size:25px;font-weight:600}
.divider{position:absolute;display:flex;align-items:center;gap:6px}
.divider i{display:block;width:34px;border-top:2px dotted var(--blue)}
.divider b{display:block;width:12px;height:12px;border:2px solid var(--blue);border-radius:50%}

/* header */
.site-header{position:absolute;top:0;left:0;width:1200px;height:73px;background:rgba(24,27,44,.88);z-index:5}
.brand{position:absolute;left:0;top:0;width:292px;height:73px;background:linear-gradient(90deg,#2a44b8,#2f4fcf);border-radius:0 40px 40px 0;display:flex;align-items:center;padding-left:56px;gap:14px}
.brand-mark{width:34px;height:34px;border-radius:50%;border:2px solid var(--white)}
.brand-name{color:var(--white);font-weight:600;font-size:17px;line-height:19px}
.nav{position:absolute;left:0;top:0;height:73px}
.nav a{position:absolute;top:28px;font-size:13px;color:var(--white);text-decoration:none}
.nav a.active{color:#6d8cff}
.nav a.active::after{content:"";position:absolute;left:-12px;right:-12px;top:43px;border-top:3px solid var(--blue-bright)}
.call{position:absolute;left:932px;top:22px;font-family:'Oswald',sans-serif;font-size:21px;color:var(--white);display:flex;align-items:center;gap:8px}
.call span{color:#4a6df0}

/* hero */
.hero{position:absolute;top:0;left:0;width:1200px;height:648px;background:linear-gradient(100deg,#4e3b2c 0%,#6e5846 35%,#8a7564 60%,#5a4a44 100%)}
.hero-shade{position:absolute;inset:0;background:rgba(20,22,34,.35)}
.hero-kicker{position:absolute;left:87px;top:255px;color:var(--white);font-size:16px}
.hero-title{position:absolute;left:87px;top:316px;color:var(--white);font-size:32px;font-weight:500;line-height:45px}

/* about */
.about-photo{left:0;top:600px;width:440px;height:440px;background:linear-gradient(180deg,#9a6a3e 0%,#c08a4f 35%,#6f7f86 70%,#3e4a52 100%);z-index:2}
.about-title{position:absolute;left:498px;top:696px;font-size:25px;font-weight:600}
.about-lead{position:absolute;left:498px;top:775px;width:610px;font-size:13px;line-height:22px;color:var(--ink)}
.about-body{position:absolute;left:498px;top:836px;width:610px;font-size:12.5px;line-height:23px;color:var(--grey)}

/* services */
.services{position:absolute;top:1040px;left:0;width:1200px;height:550px;background:linear-gradient(90deg,#22253a,#2c2f44 50%,#232638)}
.services .section-title{top:48px;color:var(--white)}
.services-intro{position:absolute;left:240px;top:125px;width:720px;text-align:center;color:var(--white);font-size:13px;line-height:25px}
.service-card{position:absolute;top:208px;width:305px;height:213px}
.service-label{position:absolute;left:0;top:157px;width:266px;height:35px;background:var(--blue);border-radius:0 18px 18px 0;color:var(--white);font-size:14px;display:flex;align-items:center;padding-left:14px}

/* work */
.work-grid{position:absolute;left:87px;top:1732px;width:1026px;height:412px;display:grid;grid-template-columns:repeat(5,1fr);grid-template-rows:repeat(2,1fr)}
.work-tile{position:relative}
.work-overlay{position:absolute;inset:0;background:rgba(44,75,209,.85);display:flex;align-items:center;justify-content:center}
.work-overlay .frame{position:absolute;inset:22px;border:1px solid rgba(255,255,255,.8)}
.work-overlay span{color:var(--white);font-size:15px}

/* testimonial */
.testimonial{position:absolute;top:2275px;left:0;width:1200px;height:305px;background:linear-gradient(90deg,#1d2033,#282b3f 55%,#1f2235)}
.quote-text{position:absolute;left:230px;top:86px;width:740px;text-align:center;color:var(--white);font-size:13px;line-height:21px}
.quote-name{position:absolute;left:0;width:1200px;top:210px;text-align:center;color:#4a6df0;font-size:14px}
.quote-role{position:absolute;left:0;width:1200px;top:234px;text-align:center;color:var(--white);font-size:12.5px}

/* news */
.news-card{position:absolute;top:2722px;width:325px}
.news-photo{width:100%;height:194px}
.news-date{position:absolute;top:183px;left:50%;transform:translateX(-50%);background:var(--navy);color:var(--white);font-size:11px;padding:3px 18px;border-radius:12px}
.news-title{margin-top:34px;text-align:center;font-size:18px;line-height:27px;color:var(--grey)}
.news-title.active{color:var(--blue);text-decoration:underline}

/* footer */
.footer{position:absolute;top:3061px;left:0;width:1200px;height:375px;background:var(--navy)}
.footer h4{position:absolute;top:57px;font-size:14px;font-weight:500;color:var(--white)}
.footer .divider i{width:22px;border-top:1px solid #aab}
.footer .divider b{border-color:#aab;width:10px;height:10px}
.footer-address{position:absolute;left:174px;top:132px;color:#c9cad3;font-size:13px;line-height:23px}
.footer-call{position:absolute;left:174px;top:202px;font-family:'Oswald',sans-serif;font-size:20px;color:var(--white);display:flex;gap:8px;align-items:center}
.footer-mail{position:absolute;left:174px;top:236px;color:#c9cad3;font-size:13px}
.social{position:absolute;top:286px;width:28px;height:28px;border-radius:50%;border:1px solid #8d8fa0}
.social.on{background:var(--blue);border-color:var(--blue)}
.contact-form{position:absolute;left:615px;top:3194px;width:411px;height:310px;background:var(--white);box-shadow:0 4px 18px rgba(0,0,0,.18);z-index:3}
.field{position:absolute;left:19px;width:373px;height:37px;border:1px solid var(--line);font-size:12px;color:var(--grey);padding:10px 10px}
.send{position:absolute;left:19px;top:254px;width:128px;height:36px;background:var(--blue);border-radius:18px;color:var(--white);font-size:13px;display:flex;align-items:center;justify-content:center;gap:8px}
.bottom{position:absolute;top:3436px;left:0;width:1200px;height:193px;background:var(--light)}
.bottom-brand{position:absolute;left:174px;top:52px;display:flex;align-items:center;gap:16px}
.bottom-brand .mark{width:52px;height:52px;border-radius:50%;border:3px solid var(--navy)}
.bottom-brand .name{font-size:20px;font-weight:500;line-height:24px;letter-spacing:1px;color:var(--navy)}
.bottom-rule{position:absolute;left:174px;top:121px;width:940px;border-top:1px solid #c5c7cf}
.copyright{position:absolute;left:174px;top:150px;font-size:12.5px;color:var(--grey)}
</style>
</head>
<body>

<div class="hero" role="img" aria-label="Locksmith fitting a lock into a wooden door">
  <div class="hero-shade"></div>
</div>

<header class="site-header">
  <div class="brand"><div class="brand-mark"></div><div class="brand-name">Corbett Row<br>Locksmiths</div></div>
  <nav class="nav">
    <a class="active" style="left:351px">Home</a>
    <a style="left:413px">About Us</a>
    <a style="left:498px">Services</a>
    <a style="left:580px">Work</a>
    <a style="left:634px">Testimonials</a>
    <a style="left:748px">News</a>
    <a style="left:809px">Contact Us</a>
  </nav>
  <div class="call"><span>CALL US</span>
    <svg width="18" height="18" viewBox="0 0 24 24"><path d="M6.6 10.8a15 15 0 006.6 6.6l2.2-2.2c.3-.3.7-.4 1-.2 1.1.4 2.3.6 3.6.6.6 0 1 .4 1 1V20c0 .6-.4 1-1 1A17 17 0 013 4c0-.6.4-1 1-1h3.5c.6 0 1 .4 1 1 0 1.3.2 2.5.6 3.6.1.3 0 .7-.2 1z" fill="#4a6df0"/></svg>
    (03) 5550 0142</div>
</header>

<div class="hero-kicker">Welcome to Corbett Row Locksmiths</div>
<h1 class="hero-title">Master Keys Systems,Commercial<br>And Domestic Services</h1>
<div class="pill-btn" style="left:87px;top:422px;width:150px;height:36px;background:var(--blue);color:var(--white)">Explore More</div>
<div class="arrow-btn dark" style="left:22px;top:342px"><svg width="12" height="12" viewBox="0 0 12 12"><path d="M8 1L3 6l5 5" stroke="#fff" stroke-width="2" fill="none"/></svg></div>
<div class="arrow-btn blue" style="left:1141px;top:342px"><svg width="12" height="12" viewBox="0 0 12 12"><path d="M4 1l5 5-5 5" stroke="#fff" stroke-width="2" fill="none"/></svg></div>

<!-- About -->
<div class="photo about-photo" role="img" aria-label="Arched roof of the city railway station platforms"></div>
<h2 class="about-title">About Us</h2>
<div class="divider" style="left:498px;top:740px"><i></i><b></b><i></i></div>
<p class="about-lead">There are many variations of passages of Lorem Ipsum available, but the majority have suffered alteration in some form.</p>
<p class="about-body">words which don't look even slightly believable. If you are going to use a passage of Lorem Ipsum, you need to be sure there isn't anything embarrassing hidden in the middle of text. All the Lorem Ipsum generators on the Internet tend to repeat predefined chunks as necessary, making...</p>
<div class="pill-btn" style="left:498px;top:947px;width:150px;height:36px;border:1.5px solid var(--navy);color:var(--ink)">Discover More</div>

<!-- Services -->
<section class="services">
  <h2 class="section-title">Our Services</h2>
  <div class="divider" style="left:554px;top:90px"><i></i><b></b><i></i></div>
  <p class="services-intro">There are many variations of passages of Lorem Ipsum available, but the majority have suffered alteration in some form, by injected humour, or randomised words which.</p>
  <div class="service-card" style="left:106px" role="img" aria-label="Driver holding a car key at the wheel"><div style="position:absolute;inset:0;background:linear-gradient(160deg,#c9cfd6,#5b6068)"></div><div class="service-label">Automotive Locksmithing</div></div>
  <div class="service-card" style="left:457px" role="img" aria-label="Remote car key with buttons"><div style="position:absolute;inset:0;background:linear-gradient(160deg,#3a3c44,#0e0f13)"></div><div class="service-label">Master Keys Systems</div></div>
  <div class="service-card" style="left:808px" role="img" aria-label="Key in a door lock"><div style="position:absolute;inset:0;background:linear-gradient(90deg,#e4e2dc,#b79778 60%,#7a4e30)"></div><div class="service-label">Commercial Work</div></div>
  <div class="arrow-btn white" style="left:21px;top:297px"><svg width="14" height="12" viewBox="0 0 14 12"><path d="M6 1L1 6l5 5M1 6h12" stroke="#222" stroke-width="1.8" fill="none"/></svg></div>
  <div class="arrow-btn blue" style="left:1141px;top:297px"><svg width="14" height="12" viewBox="0 0 14 12"><path d="M8 1l5 5-5 5M13 6H1" stroke="#fff" stroke-width="1.8" fill="none"/></svg></div>
  <div class="pill-btn" style="left:535px;top:460px;width:130px;height:36px;border:1.5px solid var(--white);color:var(--white)">View All</div>
</section>

<!-- Featured work -->
<h2 class="section-title" style="top:1638px">Our Featured Work</h2>
<div class="divider" style="left:554px;top:1680px"><i></i><b></b><i></i></div>
<div class="work-grid">
  <div class="work-tile" role="img" aria-label="Locksmith fitting a door handle" style="background:linear-gradient(160deg,#d9cfc2,#7c6a58)"></div>
  <div class="work-tile" role="img" aria-label="Commercial lock work" style="background:#8ba0c4"><div class="work-overlay"><div class="frame"></div><span>Commercial</span></div></div>
  <div class="work-tile" role="img" aria-label="Hand using a keypad safe" style="background:linear-gradient(160deg,#e7e7e7,#8d8d90)"></div>
  <div class="work-tile" role="img" aria-label="Car key on a green background" style="background:linear-gradient(160deg,#9bc36a,#3f6a24)"></div>
  <div class="work-tile" role="img" aria-label="Locksmith working on a door lock" style="background:linear-gradient(160deg,#c9a57a,#5e4a3a)"></div>
  <div class="work-tile" role="img" aria-label="Tools picking a lock" style="background:linear-gradient(160deg,#b9b6b1,#4f4b47)"></div>
  <div class="work-tile" role="img" aria-label="Locksmith at a front door" style="background:linear-gradient(160deg,#7f8a7a,#2d3530)"></div>
  <div class="work-tile" role="img" aria-label="Keys on a ring in a lock" style="background:linear-gradient(160deg,#f2f2f2,#a3a3a6)"></div>
  <div class="work-tile" role="img" aria-label="Remote car key close up" style="background:linear-gradient(160deg,#4a4c53,#101114)"></div>
  <div class="work-tile" role="img" aria-label="Driver inside a car" style="background:linear-gradient(160deg,#dfe3e7,#5a6f8a)"></div>
</div>
<div class="pill-btn" style="left:525px;top:2183px;width:150px;height:36px;background:var(--blue);color:var(--white)">See All Work</div>

<!-- Testimonial -->
<section class="testimonial">
  <svg class="abs" style="left:0;top:0" width="1200" height="305" viewBox="0 0 1200 305">
    <path d="M118 48 h12 l-6 22 h-8z M138 48 h12 l-6 22 h-8z" fill="#fff"/>
    <path d="M1052 180 h12 l-6 22 h-8z M1072 180 h12 l-6 22 h-8z" fill="#fff" transform="rotate(180 1068 191)"/>
    <path d="M170 53 H1068 l-60 20" stroke="#8b8d9c" stroke-width="1" fill="none"/>
    <path d="M1030 180 H132 l60 -20" stroke="#8b8d9c" stroke-width="1" fill="none"/>
    <path d="M58 116 H38 M44 110 l-6 6 6 6" stroke="#fff" stroke-width="2" fill="none"/>
    <path d="M1142 116 H1162 M1156 110 l6 6 -6 6" stroke="#fff" stroke-width="2" fill="none"/>
    <rect x="1138" y="110" width="4" height="12" fill="#3b5fe0"/>
  </svg>
  <p class="quote-text">Contrary to popular belief, Lorem Ipsum is not simply random text. It has roots in a piece of classical Latin literature from 45 BC, making it over 2000 years old. Daniel Harrow, a Latin professor at Westbrook College in Virginia, looked up...</p>
  <div class="quote-name">Standard Chunk</div>
  <div class="quote-role">Generate Combined Sentence</div>
</section>

<!-- News -->
<h2 class="section-title" style="top:2626px">Latest News</h2>
<div class="divider" style="left:554px;top:2667px"><i></i><b></b><i></i></div>
<div class="news-card" style="left:87px">
  <div class="news-photo" role="img" aria-label="Locksmith fixing a door lock" style="background:linear-gradient(160deg,#b07a46,#4d5e8a)"></div>
  <div class="news-date">Aug-16-2016</div>
  <p class="news-title">How You Feels in Your<br>Room Lock...</p>
</div>
<div class="news-card" style="left:438px">
  <div class="news-photo" role="img" aria-label="Hand opening a car door handle" style="background:linear-gradient(160deg,#d2d6dc,#7b8593)"></div>
  <div class="news-date">Aug-16-2016</div>
  <p class="news-title active">Best Lock Trends 2016<br>Mauris</p>
</div>
<div class="news-card" style="left:789px">
  <div class="news-photo" role="img" aria-label="Hands fitting a brass door knob" style="background:linear-gradient(160deg,#e6c79e,#9a6a3c)"></div>
  <div class="news-date">Aug-16-2016</div>
  <p class="news-title">Best Before Your Lock<br>Repair...</p>
</div>
<div class="arrow-btn white" style="left:21px;top:2801px"><svg width="14" height="12" viewBox="0 0 14 12"><path d="M6 1L1 6l5 5M1 6h12" stroke="#222" stroke-width="1.8" fill="none"/></svg></div>
<div class="arrow-btn blue" style="left:1141px;top:2801px"><svg width="14" height="12" viewBox="0 0 14 12"><path d="M8 1l5 5-5 5M13 6H1" stroke="#fff" stroke-width="1.8" fill="none"/></svg></div>

<!-- Footer -->
<footer class="footer">
  <h4 style="left:174px">Contact Us</h4>
  <div class="divider" style="left:174px;top:86px"><i></i><b></b><i></i></div>
  <p class="footer-address">Corbett Row Locksmiths<br>18 Harbour Lane, 3000 Melbourne<br>Australia</p>
  <div class="footer-call">Call Us
    <svg width="18" height="18" viewBox="0 0 24 24"><path d="M6.6 10.8a15 15 0 006.6 6.6l2.2-2.2c.3-.3.7-.4 1-.2 1.1.4 2.3.6 3.6.6.6 0 1 .4 1 1V20c0 .6-.4 1-1 1A17 17 0 013 4c0-.6.4-1 1-1h3.5c.6 0 1 .4 1 1 0 1.3.2 2.5.6 3.6.1.3 0 .7-.2 1z" fill="#4a6df0"/></svg>
    (03) 5550 0142</div>
  <p class="footer-mail">hello@corbettrowlocks.example</p>
  <div class="social" style="left:178px"></div>
  <div class="social on" style="left:220px"></div>
  <div class="social" style="left:262px"></div>
  <div class="social" style="left:304px"></div>
  <h4 style="left:615px">Get In Touch</h4>
  <div class="divider" style="left:615px;top:86px"><i></i><b></b><i></i></div>
</footer>

<form class="contact-form">
  <div class="field" style="top:19px">Name:</div>
  <div class="field" style="top:63px">Phone:</div>
  <div class="field" style="top:107px">Email:</div>
  <div class="field" style="top:151px;height:84px">Message:</div>
  <div class="send"><svg width="14" height="14" viewBox="0 0 14 14"><path d="M1 7L13 1 10 13 7 8z" fill="#fff"/></svg>Send</div>
</form>

<div class="bottom">
  <div class="bottom-brand"><div class="mark"></div><div class="name">Corbett Row<br>Locksmiths</div></div>
  <div class="bottom-rule"></div>
  <p class="copyright">Copyright 2017 Corbett Row Locksmiths. All Rights Reserved.</p>
  <svg class="abs" style="left:1006px;top:142px" width="20" height="22" viewBox="0 0 20 22"><path d="M10 15V2M4 8l6-6 6 6M2 20h16" stroke="#2c4bd1" stroke-width="2.2" fill="none"/></svg>
</div>

</body>
</html>
```